Tress Radiant from root to soul. Hair stylist that specializes in extensions.

I am Marisol I am a hair stylist and I would like a website designed for my hair business.

I currently book clients via my profile on glamslot.net/marisolbreck

I need a professional website ( tressradiantfromroottosoul.net ) to display photos and prices for services offered.

I would like to have a home page with a brief bio, Image with logo and testimonials at the bottom, and a header with tab that include: menu of services, gallery,and FAQs.

On the "Services" page, I'm not interested in photos on this page. Just the name of the service, brief description, and pricing. I would also like to have, on this page, "Appointment Request" with fields that include: Name, service requested, desired time frame (morning, afternoon, evening), and contact number and email

On the "Gallery" page, I would like pictures only, but arranged and/or presented in a creative way...

Target Market(s)

Women ages 25-55 who interested in hair extension services.

Industry/Entity Type

Hair And Beauty

Coding

Coded - Design and coding required

Number of Pages Required

5+ page

Font styles to use
Sans Serif

Requirements
Must have
• Must include tabs that include, Menu of services offered, a quik pae link to pay deposits with ease, location, contact information, photo gallery, and policy/faqs.
Nice to have
• If possible i would like to stream music with the ability to be silenced. I would like a neutral color palette tans and beige.
Should not have
• stock images

```html
<!DOCTYPE html>
<html lang="en">
<head>
<meta charset="utf-8">
<title>Tress Radiant from root to soul</title>
<link rel="stylesheet" href="https://fonts.googleapis.com/css2?family=Lato:wght@300;400;700;900&family=Open+Sans:wght@400;600&display=swap">
<style>
:root{
  --tan:#c3ab7f;
  --tan-deep:#b19562;
  --tan-dark:#9a7f4f;
  --ink:#2b2826;
  --ink-deep:#1c1a19;
  --cream:#f7f4ef;
  --line:#e3dccf;
  --text:#6f6a63;
  --white:#ffffff;
}
*{box-sizing:border-box;margin:0;padding:0}
html,body{width:1200px;height:3704px;overflow:hidden}
body{font-family:"Open Sans",Arial,sans-serif;color:var(--text);background:var(--white);position:relative;font-size:13px}
.head{font-family:"Lato",Arial,sans-serif}
.block{position:absolute;left:0;width:1200px}
.photo{position:absolute}
/* hero */
.hero{top:0;height:675px}
.hero-photo{inset:0;background:radial-gradient(ellipse at 52% 40%,#8b847c 0%,#4e4945 35%,#252220 70%,#171514 100%)}
.brand{position:absolute;left:195px;top:22px;font-family:"Lato",sans-serif;font-weight:900;color:var(--white);font-size:20px;line-height:20px;letter-spacing:1px;text-transform:uppercase}
.nav{position:absolute;right:200px;top:34px;display:flex;gap:28px;align-items:center}
.nav a{color:var(--white);text-decoration:none;font-family:"Lato",sans-serif;font-size:13px;letter-spacing:.5px}
.nav-rule{position:absolute;left:0;right:0;top:86px;border-top:1px solid rgba(255,255,255,.15)}
.tagline{position:absolute;top:356px;width:100%;text-align:center;color:var(--white);font-family:"Lato",sans-serif;font-weight:300;font-size:36px;letter-spacing:3px;word-spacing:40px}
.btn-ghost{position:absolute;left:451px;top:452px;width:298px;height:46px;border:1px solid var(--white);color:var(--white);font-family:"Lato",sans-serif;font-size:18px;letter-spacing:1px;display:flex;align-items:center;justify-content:center}
/* contact strip */
.strip{top:675px;height:80px;background:var(--white)}
.chip{position:absolute;top:12px;height:50px;border:1px solid var(--line);display:flex;align-items:center;justify-content:center;gap:12px;font-size:12px;color:var(--text)}
/* about */
.about{top:755px;height:373px;background:linear-gradient(120deg,#fbf9f6,#f1ede6 60%,#faf8f4)}
.about-title{position:absolute;left:185px;top:50px;font-size:22px;color:var(--tan)}
.portrait{left:185px;top:100px;width:133px;height:222px;background:linear-gradient(160deg,#d59a5a,#8a5a36 60%,#3c2a20)}
.signature{left:322px;top:110px;width:60px;height:180px;background:linear-gradient(#e7e1d7,#d4ccbf)}
.about-text{position:absolute;left:405px;top:118px;width:240px;font-size:11.5px;line-height:18px}
.btn-soft{position:absolute;border:1px solid var(--line);color:#b9ad99;font-size:11px;display:flex;align-items:center;justify-content:center}
.vogue-title{position:absolute;left:740px;top:50px;font-size:22px;color:var(--tan)}
.vogue-arrows{position:absolute;left:983px;top:57px;display:flex;gap:4px}
.sq{width:18px;height:18px;background:var(--tan);color:var(--white);font-size:10px;display:flex;align-items:center;justify-content:center}
.vogue{top:95px;width:125px;height:108px}
/* services grid */
.services{top:1128px;height:802px;display:grid;grid-template-columns:400px 400px 400px;grid-template-rows:279px 286px 237px}
.cell{position:relative;text-align:center;color:var(--white);padding-top:30px}
.cell.tan{background:var(--tan)}
.cell.deep{background:var(--tan-deep)}
.cell h2{font-family:"Lato",sans-serif;font-weight:700;font-size:28px;line-height:32px;text-transform:uppercase;margin-bottom:16px}
.price{font-size:11.5px;line-height:31px}
.price span{margin-left:18px}
.btn-white{display:inline-block;margin-top:12px;background:var(--white);color:var(--tan-dark);font-size:14px;padding:6px 18px}
.cell.pic{padding:0}
.framed{position:absolute;inset:10px;border:1px solid rgba(255,255,255,.35)}
/* faq band */
.faqband{top:1930px;height:405px;background:linear-gradient(110deg,#faf8f4,#efeae2 55%,#f9f7f3)}
.col-title{position:absolute;top:40px;font-size:22px;color:var(--tan)}
.faq-open{position:absolute;left:172px;top:85px;width:252px;height:34px;background:var(--tan-dark);color:var(--white);font-size:11px;display:flex;align-items:center;justify-content:space-between;padding:0 12px}
.faq-body{position:absolute;left:172px;top:119px;width:252px;height:102px;background:var(--white);padding:14px;font-size:11px;line-height:16px}
.faq-item{position:absolute;left:172px;width:252px;height:32px;background:var(--tan);color:var(--white);font-size:11px;display:flex;align-items:center;justify-content:space-between;padding:0 12px}
.testi{position:absolute;left:465px;top:118px;width:270px;height:190px;background:var(--white);border:1px solid var(--line);padding:30px 22px;font-size:11px;line-height:16px;font-style:italic}
.testi-by{position:absolute;left:22px;bottom:24px;font-style:normal;color:var(--tan);font-size:10px}
.testi-arrows{position:absolute;left:680px;top:85px;display:flex;gap:4px}
.video{left:758px;top:120px;width:268px;height:200px;background:radial-gradient(circle at 50% 45%,#9a7553,#4b3627 60%,#1f1714)}
.video-label{position:absolute;left:770px;top:124px;color:var(--white);font-size:11px;font-weight:600}
.video-bar{position:absolute;left:758px;top:290px;width:268px;height:30px;background:rgba(0,0,0,.55)}
/* straight band */
.straight{top:2335px;height:383px;background:var(--ink)}
.straight-photo{left:690px;top:0;width:420px;height:383px;background:linear-gradient(90deg,var(--ink) 0%,#6d4a2c 30%,#c08a52 60%,#7a5332 85%,var(--ink) 100%)}
.straight h2{position:absolute;left:190px;top:70px;font-family:"Lato",sans-serif;font-weight:700;font-size:40px;line-height:50px;color:var(--tan);text-transform:uppercase}
.straight p{position:absolute;left:190px;top:205px;width:430px;font-size:12px;line-height:20px;color:#7f7a73}
.btn-line{position:absolute;left:190px;top:283px;width:170px;height:32px;border:1px solid var(--tan);color:var(--tan);font-size:12px;display:flex;align-items:center;justify-content:center}
/* gallery */
.gallery{top:2718px;height:392px;background:linear-gradient(100deg,#f9f7f3,#eee9e1 50%,#f9f7f3)}
.gallery h2{position:absolute;top:36px;width:100%;text-align:center;font-family:"Lato",sans-serif;font-weight:400;font-size:34px;color:var(--tan)}
.gal{top:112px;width:272px;height:230px}
.chev{position:absolute;top:190px}
/* contact */
.contact{top:3110px;height:340px}
.contact-side{position:absolute;left:0;top:0;width:600px;height:340px;background:var(--tan);color:var(--white)}
.contact-side h2{position:absolute;left:163px;top:72px;font-family:"Lato",sans-serif;font-weight:700;font-size:20px;text-transform:uppercase}
.c-line{position:absolute;display:flex;gap:14px;font-size:16px;line-height:22px}
.map{left:600px;top:0;width:600px;height:340px;background:linear-gradient(135deg,#eeebe4,#e2ddd3)}
/* footer */
.footer{top:3450px;height:254px;background:var(--ink-deep);color:#8d8780}
.f-title{position:absolute;top:50px;font-family:"Lato",sans-serif;color:#d9d2c6;font-size:14px;letter-spacing:1px;text-transform:uppercase}
.f-links{position:absolute;top:82px;font-size:11px;line-height:15px}
.f-input{position:absolute;left:615px;top:126px;width:140px;height:18px;border:1px solid #4a4541;font-size:9px;padding:2px 5px}
.f-go{position:absolute;left:758px;top:126px;width:34px;height:18px;background:var(--tan);color:var(--white);font-size:9px;display:flex;align-items:center;justify-content:center}
.card{position:absolute;top:86px;width:48px;height:30px;border-radius:3px}
.f-rule{position:absolute;left:178px;right:178px;top:198px;border-top:1px solid #34302d}
.f-copy{position:absolute;left:178px;top:214px;font-size:10px}
</style>
</head>
<body>

<header class="block hero">
  <div class="photo hero-photo" role="img" aria-label="Portrait of a woman with long voluminous silver curls"></div>
  <div class="brand">Tress Radiant<br>from root to soul</div>
  <nav class="nav">
    <a href="#about">ABOUT</a><a href="#services">SERVICES</a><a href="#gallery">GALLERY</a><a href="#faq">FAQ</a><a href="#contact">CONTACT</a>
    <svg width="14" height="14" viewBox="0 0 14 14"><circle cx="6" cy="6" r="4.5" fill="none" stroke="#fff" stroke-width="1.6"/><line x1="9.3" y1="9.3" x2="13" y2="13" stroke="#fff" stroke-width="1.6"/></svg>
  </nav>
  <div class="nav-rule"></div>
  <div class="tagline">CREATIVE CLASSIC DISTINGUISHED</div>
  <div class="btn-ghost">MAKE AN APPOINTMENT</div>
</header>

<section class="block strip">
  <div class="chip" style="left:170px;width:290px">
    <svg width="18" height="13" viewBox="0 0 18 13"><rect x="0.5" y="0.5" width="17" height="12" fill="none" stroke="#c3ab7f"/><polyline points="1,1 9,7 17,1" fill="none" stroke="#c3ab7f"/></svg>
    info@tressradiantfromroottosoul.net</div>
  <div class="chip" style="left:464px;width:270px">
    <svg width="14" height="14" viewBox="0 0 14 14"><path d="M3 1l2 3-1.5 1.5a8 8 0 0 0 5 5L10 9l3 2-1 2.5C6 13 1 8 .5 2z" fill="#c3ab7f"/></svg>
    +555-214-7730</div>
  <div class="chip" style="left:756px;width:271px">
    <svg width="12" height="16" viewBox="0 0 12 16"><path d="M6 0a6 6 0 0 1 6 6c0 4-6 10-6 10S0 10 0 6a6 6 0 0 1 6-6z" fill="#c3ab7f"/><circle cx="6" cy="6" r="2" fill="#fff"/></svg>
    <span>1840 Linden Way, Suite 7<br>Cedar Falls, TX, 75999</span></div>
</section>

<section class="block about" id="about">
  <h2 class="about-title head" style="font-weight:400">Tress Radiant from root to soul By Marisol H.</h2>
  <div class="photo portrait" role="img" aria-label="Portrait of stylist Marisol with long copper hair"></div>
  <div class="photo signature" role="img" aria-label="Handwritten signature of Marisol"></div>
  <p class="about-text">Creative. Classic. Distinguished. These are just a few attributes that Marisol embodies, received in depth training from Halvern Academy of Hair Design, where I had the opportunity to pair my experience with advanced technical training. My passion for art and design has given me the opportunity to express myself through hair design.</p>
  <div class="btn-soft" style="left:405px;top:280px;width:155px;height:38px">Know More &nbsp;›</div>
  <h2 class="vogue-title head" style="font-weight:400">Styles in Vogue</h2>
  <div class="vogue-arrows"><div class="sq">‹</div><div class="sq">›</div></div>
  <div class="photo vogue" style="left:735px;background:linear-gradient(150deg,#ecd7a4,#b58d55)" role="img" aria-label="Blonde layered bob style"></div>
  <div class="photo vogue" style="left:865px;background:linear-gradient(150deg,#4a3426,#a0703c)" role="img" aria-label="Dark side-swept style with highlights"></div>
  <div class="photo vogue" style="left:735px;top:213px;background:linear-gradient(150deg,#d8c39a,#7d6248)" role="img" aria-label="Short pixie cut style"></div>
  <div class="photo vogue" style="left:865px;top:213px;background:linear-gradient(150deg,#c57a44,#6e3a22)" role="img" aria-label="Auburn straight style"></div>
</section>

<section class="block services" id="services">
  <div class="cell tan">
    <h2>Basic Services</h2>
    <div class="price">Blowout Style &nbsp;(1 hr., 30 min.)<span>$45 and up</span></div>
    <div class="price">Custom Cut Design &nbsp;(30 min.)<span>$35</span></div>
    <div class="price">Wand curls &nbsp;(45 min.)<span>$25</span></div>
    <div class="btn-white">Book An Appointment</div>
  </div>
  <div class="cell pic" role="img" aria-label="Woman with layered brunette hair and golden highlights" style="background:linear-gradient(160deg,#d9c8b0,#7c5a3c 55%,#3b2a1f)"></div>
  <div class="cell tan">
    <h2>Color Services</h2>
    <div class="price">High &amp; Low Lights &nbsp;(2 hr.)<span>$130 and up</span></div>
    <div class="price">Permanent Color &nbsp;(60 min.)<span>$125 and up</span></div>
    <div class="price">Semi-permanent color &nbsp;(1 hr., 45 min.)<span>$25 and up</span></div>
    <div class="btn-white">Book An Appointment</div>
  </div>
  <div class="cell pic" role="img" aria-label="Woman with voluminous natural curls" style="background:linear-gradient(160deg,#9a9591,#4a3428 55%,#2a1e18)"><div class="framed"></div></div>
  <div class="cell deep">
    <h2>Extensions</h2>
    <div class="price">Custom Extensions &nbsp;(3 hr.)<span>$185 and up</span></div>
    <div class="price">Extension coloring per bundle &nbsp;(45 min.)<span>$25</span></div>
    <div class="price">extension removal + reinstallation &nbsp;(4 hr.)<span>$240 and up</span></div>
    <div class="btn-white">Book An Appointment</div>
  </div>
  <div class="cell pic" role="img" aria-label="Woman with long flowing dark hair in motion" style="background:linear-gradient(160deg,#c8bfb6,#6a4a38 55%,#3a2a22)"><div class="framed"></div></div>
  <div class="cell tan">
    <h2>Extension<br>Removal</h2>
    <div class="price">(1 hr., 15 min.)<span>$75 and up</span></div>
    <div class="btn-white">Book An Appointment</div>
  </div>
  <div class="cell pic" role="img" aria-label="Angled bob haircut with blonde balayage, back view" style="background:linear-gradient(160deg,#d4cfc8,#9c7a56 55%,#5a4030)"><div class="framed"></div></div>
  <div class="cell tan">
    <h2>Straightening<br>Services</h2>
    <div class="price">Chemical Straightener &nbsp;(1 hr., 30 min.)<span>$65</span></div>
    <div class="price">Silk Press &nbsp;(1 hr., 30 min.)<span>$65</span></div>
    <div class="btn-white">Book An Appointment</div>
  </div>
</section>

<section class="block faqband" id="faq">
  <h2 class="col-title head" style="left:185px;font-weight:400">FAQ</h2>
  <div class="faq-open">HOW EARLY SHOULD I BOOK AHEAD <span>−</span></div>
  <p class="faq-body">Please book at least one week ahead for extension services so we can order hair in your shade, texture and length before your visit and plan enough chair time.</p>
  <div class="faq-item" style="top:231px">DO YOU TAKE WALK INS <span>+</span></div>
  <div class="faq-item" style="top:266px">HOW LONG DO THEY LAST <span>+</span></div>
  <div class="faq-item" style="top:301px">WHAT IS THE DEPOSIT <span>+</span></div>
  <div class="faq-item" style="top:336px">CAN I BRING MY OWN HAIR <span>+</span></div>

  <h2 class="col-title head" style="left:478px;font-weight:400">Testimonials</h2>
  <div class="testi-arrows"><div class="sq">‹</div><div class="sq">›</div></div>
  <div class="testi">" I have been looking for a stylist since I moved to Cedar Falls for 7 years. I noticed a young lady's hair and she gave me Marisol's information. I LOVE MY HAIR. She does an amazing job. Always leave satisfied!!"
    <div class="testi-by">&#9679; Renata V. &nbsp; &#9679; 2/09/15</div></div>

  <h2 class="col-title head" style="left:765px;font-weight:400">Featured Video</h2>
  <div class="photo video" role="img" aria-label="Video still of a woman with long bronze curls"></div>
  <div class="video-label">Beautiful Hair</div>
  <div class="video-bar">
    <svg width="268" height="30" viewBox="0 0 268 30"><polygon points="12,9 12,21 21,15" fill="#fff"/><rect x="32" y="14" width="150" height="3" fill="#8a8580"/><rect x="32" y="14" width="40" height="3" fill="#fff"/><rect x="200" y="11" width="14" height="8" fill="#fff"/><rect x="225" y="14" width="28" height="3" fill="#fff"/></svg>
  </div>
</section>

<section class="block straight">
  <div class="photo straight-photo" role="img" aria-label="Woman with sleek straight honey brown hair and blunt bangs"></div>
  <h2>Straight Hair,<br>Beautiful You...</h2>
  <p>I also specialize in natural straightening and I assist many clients who are transitioning from relaxed to natural hair.</p>
  <div class="btn-line">MAKE AN APPOINTMENT</div>
</section>

<section class="block gallery" id="gallery">
  <h2>Our Gallery</h2>
  <svg class="chev" style="left:72px" width="22" height="60" viewBox="0 0 22 60"><polyline points="20,2 2,30 20,58" fill="none" stroke="#555" stroke-width="1.5"/></svg>
  <div class="photo gal" style="left:170px;background:linear-gradient(135deg,#c79a6a,#6b4a34 60%,#3a2a22)" role="img" aria-label="Collage of brunette wavy extension styles"></div>
  <div class="photo gal" style="left:463px;background:linear-gradient(135deg,#3d2f28,#d3b07a 55%,#8b6a48)" role="img" aria-label="Collage of blonde and dark curled styles"></div>
  <div class="photo gal" style="left:756px;background:linear-gradient(135deg,#2a1d16,#7a4e2e 55%,#3a261a)" role="img" aria-label="Close view of long dark spiral curls"></div>
  <svg class="chev" style="left:1096px" width="22" height="60" viewBox="0 0 22 60"><polyline points="2,2 20,30 2,58" fill="none" stroke="#555" stroke-width="1.5"/></svg>
</section>

<section class="block contact" id="contact">
  <div class="contact-side">
    <h2>Tress Radiant from root to soul</h2>
    <div class="c-line" style="left:228px;top:122px">
      <svg width="12" height="16" viewBox="0 0 12 16"><path d="M6 0a6 6 0 0 1 6 6c0 4-6 10-6 10S0 10 0 6a6 6 0 0 1 6-6z" fill="#fff"/><circle cx="6" cy="6" r="2" fill="#c3ab7f"/></svg>
      <span>1840 Linden Way, Suite 7<br>Cedar Falls, TX, 75999</span></div>
    <div class="c-line" style="left:272px;top:200px">
      <svg width="14" height="14" viewBox="0 0 14 14"><path d="M3 1l2 3-1.5 1.5a8 8 0 0 0 5 5L10 9l3 2-1 2.5C6 13 1 8 .5 2z" fill="#fff"/></svg>
      555-214-7730</div>
    <div class="c-line" style="left:178px;top:238px">
      <svg width="18" height="13" viewBox="0 0 18 13"><rect x="0.5" y="0.5" width="17" height="12" fill="#fff"/><polyline points="1,1 9,7 17,1" fill="none" stroke="#c3ab7f"/></svg>
      info@tressradiantfromroottosoul.net</div>
  </div>
  <div class="photo map" role="img" aria-label="Street map showing the salon location"></div>
</section>

<footer class="block footer">
  <div class="f-title" style="left:178px">Links</div>
  <div class="f-links" style="left:178px">History<br>Concept<br>Process<br>Promises<br>Location</div>
  <div class="f-links" style="left:268px">Quik Pae Link<br>FAQ<br>News<br>Blog<br>Policy &amp; Terms</div>
  <div class="f-title" style="left:398px">Social Media</div>
  <div class="f-links" style="left:398px">Stay Connected with us</div>
  <svg style="position:absolute;left:398px;top:108px" width="160" height="14" viewBox="0 0 160 14">
    <circle cx="7" cy="7" r="6" fill="#8d8780"/><circle cx="30" cy="7" r="6" fill="#8d8780"/><circle cx="53" cy="7" r="6" fill="#8d8780"/><circle cx="76" cy="7" r="6" fill="#8d8780"/><circle cx="99" cy="7" r="6" fill="#8d8780"/><circle cx="122" cy="7" r="6" fill="#8d8780"/>
  </svg>
  <div class="f-title" style="left:615px">Newsletter</div>
  <div class="f-links" style="left:615px">Register your email address to<br>get latest updates from us.</div>
  <div class="f-input">your email</div>
  <div class="f-go">GO</div>
  <div class="f-title" style="left:842px">Payment Info</div>
  <div class="f-links" style="left:842px;top:70px;color:#d9d2c6">quik pae</div>
  <div class="card" style="left:842px;background:#c3ab7f"></div>
  <div class="card" style="left:894px;background:#ffffff"></div>
  <div class="card" style="left:946px;background:#8d8780"></div>
  <div class="card" style="left:998px;background:#b19562"></div>
  <div class="f-rule"></div>
  <div class="f-copy">Copyright © Tress Radiant from root to soul 2016. All rights reserved.</div>
</footer>

</body>
</html>
```